Sports nutritional supplement brand*

We need to design an integrated packaging for a sports nutritional supplement brand containing more than 30 products The design of the packaging consists of two parts, half in black color, fixed in all types, and the other half is variable. I sent you pictures containing some beautiful ideas that suit what I think of. The design must contain a place for the taste image, such as chocolate, strawberry, banana, orange, grape, watermelon The company name must be clearly visible in the middle and the location of the code and barcode

Target Market(s)

the whole world

Industry/Entity Type

Entrepreneur

Font styles to use
Decorative

Colors

Designer to choose colors to be used in the design.

Requirements
Must have
• The project consists of several types of supplements. I need each type to be different from the other in terms of a color that is constant, such as the black color and the half of the box is color changing, for example the box is made of black and red and the second box is black and yellow and the colors must be bright and 3D
Nice to have
• The outer box will be white and the box will be completely wrapped from the head neck down, not around the box There should be a small box design, a large protein box, and a protein pouch bag
Should not have

```html
<!DOCTYPE html>
<html lang="en">
<head>
<meta charset="utf-8">
<title>FitForge Supplement Pouches</title>
<link rel="stylesheet" href="https://fonts.googleapis.com/css2?family=Russo+One&family=Teko:wght@500&display=swap">
<style>
  :root {
    --bg: #ffffff;
    --black: #141414;
    --black-soft: #2a2a2a;
    --gold: #e2c21e;
    --gold-deep: #b8901a;
    --white: #f2f2f2;
    --choc-light: #c99580;
    --choc-dark: #8b4a33;
    --red-light: #ea2224;
    --red-dark: #a90e10;
  }
  * { margin: 0; padding: 0; box-sizing: border-box; }
  html, body { width: 1200px; height: 848px; overflow: hidden; background: var(--bg); }
  .canvas { position: relative; width: 1200px; height: 848px; }

  .pouch { position: absolute; top: 174px; width: 314px; height: 550px; }
  .pouch--creatine { left: 206px; }
  .pouch--whey { left: 722px; }
  .pouch__shape { position: absolute; inset: 0; }

  .pouch__brand,
  .pouch__product {
    position: absolute;
    white-space: nowrap;
    line-height: 1;
    color: var(--gold);
    transform: translate(-50%, -50%) rotate(-28deg);
  }
  .pouch__brand {
    left: 156px; top: 262px;
    font-family: "Teko", sans-serif; font-weight: 500;
    font-size: 66px; letter-spacing: 3px;
  }
  .pouch__product {
    left: 162px; top: 346px;
    font-family: "Russo One", sans-serif;
    font-size: 34px;
  }
  .pouch--whey .pouch__product { left: 168px; top: 338px; font-size: 31px; }

  .pouch__flavor-image {
    position: absolute; left: 104px; top: 400px; width: 108px; height: 68px;
    border-radius: 10px;
  }
  .pouch--creatine .pouch__flavor-image { background: linear-gradient(135deg, #6b3a2a, #2e1710); }
  .pouch--whey .pouch__flavor-image { background: radial-gradient(circle at 45% 45%, #e0323a, #8e0f14); }

  .stamp {
    position: absolute; top: 434px; width: 48px; height: 48px;
    border: 2px solid var(--gold); border-radius: 50%;
    display: flex; flex-direction: column; align-items: center; justify-content: center;
    color: var(--gold); font-family: "Teko", sans-serif; font-weight: 500; line-height: 0.9;
  }
  .stamp--natural { left: 34px; font-size: 14px; }
  .stamp--natural small { font-size: 8px; letter-spacing: 0.5px; }
  .stamp--weight { left: 222px; font-size: 19px; }

  .pouch__flavor {
    position: absolute; left: 0; right: 0; top: 480px;
    text-align: center;
    font-family: "Teko", sans-serif; font-weight: 500;
    font-size: 26px; line-height: 1; letter-spacing: 1px;
    color: var(--gold);
  }
  .pouch__label {
    position: absolute; left: 0; right: 0; top: 512px;
    text-align: center;
    font-family: "Teko", sans-serif; font-weight: 500;
    font-size: 15px; line-height: 1; letter-spacing: 3px;
    color: var(--white);
  }
</style>
</head>
<body>
<main class="canvas">

  <section class="pouch pouch--creatine">
    <svg class="pouch__shape" width="314" height="550" viewBox="0 0 314 550">
      <defs>
        <linearGradient id="chocTone" x1="0" y1="0" x2="1" y2="0">
          <stop offset="0" stop-color="var(--choc-dark)"/>
          <stop offset="0.35" stop-color="var(--choc-light)"/>
          <stop offset="1" stop-color="var(--choc-dark)"/>
        </linearGradient>
        <linearGradient id="blackTone" x1="0" y1="0" x2="1" y2="0">
          <stop offset="0" stop-color="var(--black)"/>
          <stop offset="0.6" stop-color="var(--black-soft)"/>
          <stop offset="1" stop-color="var(--black)"/>
        </linearGradient>
      </defs>
      <path d="M16 0 H298 Q314 0 314 16 V550 H0 V16 Q0 0 16 0 Z" fill="url(#chocTone)"/>
      <polygon points="0,378 314,212 314,550 0,550" fill="url(#blackTone)"/>
      <line x1="18" y1="64" x2="296" y2="64" stroke="#000" stroke-opacity="0.18" stroke-width="3"/>
      <circle cx="158" cy="134" r="36" fill="var(--gold-deep)"/>
    </svg>
    <div class="pouch__brand">FitForge</div>
    <div class="pouch__product">creatine</div>
    <div class="pouch__flavor-image" role="img" aria-label="Chocolate pieces"></div>
    <div class="stamp stamp--natural">100%<small>NATURAL</small></div>
    <div class="stamp stamp--weight">500G</div>
    <div class="pouch__flavor">CHOCOLATE</div>
    <div class="pouch__label">DETARY SUPPLEMENT</div>
  </section>

  <section class="pouch pouch--whey">
    <svg class="pouch__shape" width="314" height="550" viewBox="0 0 314 550">
      <defs>
        <linearGradient id="redTone" x1="0" y1="0" x2="1" y2="0">
          <stop offset="0" stop-color="var(--red-dark)"/>
          <stop offset="0.35" stop-color="var(--red-light)"/>
          <stop offset="1" stop-color="var(--red-dark)"/>
        </linearGradient>
        <linearGradient id="blackToneB" x1="0" y1="0" x2="1" y2="0">
          <stop offset="0" stop-color="var(--black)"/>
          <stop offset="0.6" stop-color="var(--black-soft)"/>
          <stop offset="1" stop-color="var(--black)"/>
        </linearGradient>
      </defs>
      <path d="M16 0 H298 Q314 0 314 16 V550 H0 V16 Q0 0 16 0 Z" fill="url(#redTone)"/>
      <polygon points="0,378 314,212 314,550 0,550" fill="url(#blackToneB)"/>
      <line x1="18" y1="64" x2="296" y2="64" stroke="#000" stroke-opacity="0.18" stroke-width="3"/>
      <circle cx="158" cy="134" r="36" fill="var(--gold-deep)"/>
    </svg>
    <div class="pouch__brand">FitForge</div>
    <div class="pouch__product">Whey protein</div>
    <div class="pouch__flavor-image" role="img" aria-label="Fresh strawberries"></div>
    <div class="stamp stamp--natural">100%<small>NATURAL</small></div>
    <div class="stamp stamp--weight">500G</div>
    <div class="pouch__flavor">STRAWBERRY</div>
    <div class="pouch__label">DETARY SUPPLEMENT</div>
  </section>

</main>
</body>
</html>
```